AWESOME CYBER MONDAY SALE AD NEEDED

Create a Cyber Monday ad for nitrile gloves. We are offering a box of 100, no-powder, exam grade nitrile gloves, for $9.99. No limit. Each case is $99. Create something simple, eye catching, cool. BreezeShield.com. Sale ends on December 4th. While supplies last. We are a local medical supply company in Hawaii that serves the general public in addition to local businesses, government, etc. Gloves are in short supply and we have tons of inventory ready to sell.

Target Market(s)

Businesses that use supplies such as gloves

Industry/Entity Type

medical supplies

Requirements
Must have
• The company logo, website, picture of gloves and pricing.

```html
<!DOCTYPE html>
<html lang="en">
<head>
<meta charset="utf-8">
<title>Cyber Monday Sale – BreezeShield.com</title>
<link href="https://fonts.googleapis.com/css2?family=Montserrat:ital,wght@0,700;0,800;1,800&family=Catamaran:wght@600;700&family=Exo+2:ital,wght@1,600&family=Open+Sans:wght@600&display=swap" rel="stylesheet">
<style>
  :root {
    --page: #ffffff;
    --dark-center: #4a4a4a;
    --dark-edge: #1c1c1c;
    --light-bg: #f9f9f9;
    --sky: #3aa9ea;
    --neon: #39a6f2;
    --glove-light: #5cc3f5;
    --glove-deep: #2a9fe0;
    --green: #0f8f3e;
    --white: #ffffff;
    --ink: #1b1b1b;
  }
  * { box-sizing: border-box; margin: 0; padding: 0; }
  html, body {
    width: 1200px; height: 1200px; overflow: hidden;
    background: var(--page);
  }
  .stage { position: relative; width: 1200px; height: 1200px; }

  .poster {
    position: absolute; top: 173px;
    width: 516px; height: 859px; overflow: hidden;
    box-shadow: 6px 8px 14px rgba(0,0,0,0.28);
    font-family: "Catamaran", sans-serif;
  }
  .poster--dark {
    left: 58px;
    background: radial-gradient(ellipse at 50% 42%, var(--dark-center) 0%, #333 45%, var(--dark-edge) 100%);
    color: var(--white);
  }
  .poster--light {
    left: 631px;
    background: var(--light-bg);
    color: var(--ink);
  }

  .brand-name {
    position: absolute; top: 40px; right: 16px;
    font-family: "Catamaran", sans-serif; font-weight: 700;
    font-size: 21px; letter-spacing: -0.2px;
  }
  .poster--dark .brand-name { color: var(--white); }
  .poster--light .brand-name { color: var(--green); }

  .headline { position: absolute; left: 20px; font-family: "Montserrat", sans-serif; line-height: 1; }
  .headline--cyber {
    top: 44px; font-size: 81px; font-weight: 700; letter-spacing: -1px;
  }
  .poster--dark .headline--cyber {
    color: var(--dark-edge);
    -webkit-text-stroke: 2.5px var(--neon);
    text-shadow: 0 0 10px rgba(57,166,242,0.8), 0 0 4px rgba(57,166,242,0.9);
  }
  .poster--light .headline--cyber {
    color: var(--white);
    -webkit-text-stroke: 2px var(--sky);
  }
  .headline--monday { top: 118px; left: 18px; font-size: 80px; font-weight: 800; letter-spacing: -0.5px; }
  .poster--dark .headline--monday { color: var(--white); }
  .poster--light .headline--monday { color: var(--sky); }
  .headline--sale { top: 186px; left: 22px; font-size: 63px; font-weight: 800; font-style: italic; }
  .poster--dark .headline--sale { color: var(--sky); }
  .poster--light .headline--sale { color: var(--green); }

  .product-photo {
    position: absolute; left: 164px; top: 255px; width: 352px; height: 390px;
    background: radial-gradient(ellipse at 62% 48%, var(--glove-light) 0%, var(--glove-deep) 55%, rgba(42,159,224,0) 78%);
  }

  .price-tag { position: absolute; left: 106px; top: 378px; width: 240px; height: 60px; }
  .price-tag svg { position: absolute; left: 0; top: 0; }
  .price-tag__amount {
    position: absolute; left: 16px; top: 6px;
    font-family: "Open Sans", sans-serif; font-weight: 600;
    font-size: 31px; color: var(--white); letter-spacing: 1px;
  }
  .price-note {
    position: absolute; left: 106px; top: 435px;
    font-family: "Open Sans", sans-serif; font-size: 11px; letter-spacing: -0.3px;
  }

  .features { position: absolute; left: 22px; top: 622px; list-style: none; }
  .features li {
    font-weight: 600; font-size: 20px; letter-spacing: 0.8px; line-height: 30px;
    display: flex; align-items: center;
  }
  .features .bullet::before {
    content: ""; display: inline-block; width: 8px; height: 8px;
    background: var(--sky); margin-right: 6px;
  }

  .sale-end {
    position: absolute; left: 0; right: 0; top: 745px; padding-left: 34px;
    text-align: center; font-family: "Exo 2", sans-serif; font-style: italic; font-weight: 600;
    font-size: 20px; letter-spacing: 1px; color: var(--sky);
  }

  .site-band {
    position: absolute; left: 0; right: 0; bottom: 0; height: 36px;
    background: var(--green); color: var(--white);
    display: flex; align-items: center; justify-content: center;
    font-weight: 600; font-size: 20px; letter-spacing: 6px;
  }
</style>
</head>
<body>
<div class="stage">

  <section class="poster poster--dark">
    <div class="brand-name">breezeshield</div>
    <div class="headline headline--cyber">CYBER</div>
    <div class="headline headline--monday">MONDAY</div>
    <div class="headline headline--sale">SALE</div>
    <div class="product-photo" role="img" aria-label="Photo of two blue nitrile exam gloves"></div>
    <div class="price-tag">
      <svg width="240" height="60" viewBox="0 0 240 60">
        <path d="M2 6 H112 L132 27 L112 52 H2 Z" fill="#0f8f3e" stroke="#ffffff" stroke-width="1.5"/>
        <path d="M6 10 H110 L127 27 L110 48 H6 Z" fill="none" stroke="#ffffff" stroke-width="1"/>
        <circle cx="118" cy="28" r="3" fill="#ffffff"/>
        <path d="M118 28 C150 20 170 10 193 -6 C203 8 190 20 160 28 C140 32 125 31 118 28" fill="none" stroke="#ffffff" stroke-width="1.2"/>
      </svg>
      <span class="price-tag__amount">$9.99</span>
    </div>
    <p class="price-note">No limit. Each case is $99</p>
    <ul class="features">
      <li>A Box of 100 Pieces</li>
      <li class="bullet">Powder Free Gloves</li>
      <li class="bullet">Exam Grade Nitrile Gloves</li>
    </ul>
    <p class="sale-end">Sale ends on December 4th</p>
    <div class="site-band">breezeshield.com</div>
  </section>

  <section class="poster poster--light">
    <div class="brand-name">breezeshield</div>
    <div class="headline headline--cyber">CYBER</div>
    <div class="headline headline--monday">MONDAY</div>
    <div class="headline headline--sale">SALE</div>
    <div class="product-photo" role="img" aria-label="Photo of two blue nitrile exam gloves"></div>
    <div class="price-tag">
      <svg width="240" height="60" viewBox="0 0 240 60">
        <path d="M2 6 H112 L132 27 L112 52 H2 Z" fill="#0f8f3e" stroke="#ffffff" stroke-width="1.5"/>
        <path d="M6 10 H110 L127 27 L110 48 H6 Z" fill="none" stroke="#ffffff" stroke-width="1"/>
        <circle cx="118" cy="28" r="3" fill="#ffffff"/>
      </svg>
      <span class="price-tag__amount">$9.99</span>
    </div>
    <p class="price-note">No limit. Each case is $99</p>
    <ul class="features">
      <li>A Box of 100 Pieces</li>
      <li class="bullet">Powder Free Gloves</li>
      <li class="bullet">Exam Grade Nitrile Gloves</li>
    </ul>
    <p class="sale-end">Sale ends on December 4th</p>
    <div class="site-band">breezeshield.com</div>
  </section>

</div>
</body>
</html>
```